Hemp company needs website/online store

We are a startup hemp company and we need an online storefront designed. We are very open do design, but will include our logo to help. We make 100% hemp derived products like edibles, concentrates, vapes and THCA flower. Everything is grown locally, and all products are extracted and made in house.

Requirements
Nice to have
• I would like to highlight that we have Cannabis products that are hemp derived and 100% legal across the US. Also that all cannabis is locally grown and products are extracted and made in house and sent out for third party lab testing.

```html
<!DOCTYPE html>
<html lang="en">
<head>
<meta charset="utf-8">
<title>Sunny Leaf Hemp</title>
<link href="https://fonts.googleapis.com/css2?family=Poppins:ital,wght@0,300;0,400;0,500;0,600;1,400&display=swap" rel="stylesheet">
<style>
:root{
  --green:#4a7b35;
  --green-dark:#215a1f;
  --olive:#7fa30d;
  --hero-bg:#ede7ea;
  --light:#f4f4f4;
  --text:#3c3c3c;
  --muted:#666;
  --white:#fff;
  --star:#f2b51d;
}
*{box-sizing:border-box;margin:0;padding:0}
html,body{width:1200px;height:4458px;overflow:hidden}
body{font-family:'Poppins',sans-serif;color:var(--text);background:var(--white);position:relative}
section,header,footer{position:relative;width:1200px}
.abs{position:absolute}
.btn{position:absolute;display:flex;align-items:center;justify-content:center;font-size:17px;font-weight:400}
.btn-solid{background:var(--green);color:var(--white)}
.btn-outline{border:1.5px solid var(--green);color:var(--green);background:transparent}
.photo{position:absolute}

/* header */
.site-header{height:149px;background:var(--green)}
.brand{left:88px;top:48px;display:flex;align-items:center;gap:12px;color:var(--white);font-size:30px;font-weight:500}
.brand-dot{width:34px;height:34px;border-radius:50%;background:var(--white);opacity:.9}
.nav{left:448px;top:68px;display:flex;gap:21px;font-size:15px;color:var(--white)}
.nav a{color:var(--white);text-decoration:none}
.nav .active{font-weight:600;font-size:17px;border-bottom:2px solid var(--white);padding-bottom:6px;margin-top:-4px;margin-right:12px}
.account{left:975px;top:58px;width:142px;height:44px;background:var(--white);color:var(--green);font-size:15px;font-weight:500}

/* hero */
.hero{height:544px;background:var(--hero-bg)}
.hero h1{left:80px;top:105px;width:640px;font-size:44px;line-height:50px;font-weight:500;color:var(--green)}
.hero p{left:84px;top:283px;width:630px;font-size:18px;line-height:26px;color:var(--text)}
.hero .read{left:80px;top:381px;width:177px;height:49px}
.hero .products{left:270px;top:381px;width:178px;height:49px}
.hero .leaf{left:700px;top:80px;width:470px;height:420px;border-radius:40% 60% 50% 50%;background:radial-gradient(circle at 50% 45%,#4f8a2f,#2f6a1e 55%,rgba(237,231,234,0) 72%)}

/* about */
.about{height:523px;background:var(--white)}
.about .circle{left:130px;top:80px;width:432px;height:360px;border-radius:50%;background:radial-gradient(circle at 45% 45%,#3f6d2a,#1b3a14 70%,#0f2109)}
.about .leafs{left:75px;top:180px;width:200px;height:200px;border-radius:50%;background:radial-gradient(circle,#9cc26a,rgba(156,194,106,0) 70%)}
.about h2{left:610px;top:123px;font-size:30px;font-weight:500;color:var(--green)}
.about p{left:610px;width:470px;font-size:16px;line-height:22px;color:var(--text)}
.about .p1{top:197px}
.about .p2{top:261px}
.about .explore{left:610px;top:379px;width:191px;height:42px}

/* products */
.shop{height:1356px;background:var(--light)}
.section-title{position:absolute;width:1200px;text-align:center;font-size:42px;font-weight:500;color:var(--green)}
.shop .section-title{top:72px}
.tabs{position:absolute;left:100px;top:175px;display:flex;gap:26px}
.tab{width:178px;height:47px;border:1.5px solid var(--green);color:var(--green);display:flex;align-items:center;justify-content:center;font-size:18px}
.tab.active{background:var(--green);color:var(--white);font-weight:500}
.card{position:absolute;width:338px;height:462px;background:var(--white);box-shadow:0 2px 6px rgba(0,0,0,.08)}
.card .photo{left:0;top:0;width:338px;height:220px}
.card .photo::after{content:"";position:absolute;inset:8px;border:1px solid rgba(255,255,255,.6)}
.card h3{position:absolute;top:262px;width:100%;text-align:center;font-size:21px;font-weight:500;color:var(--green)}
.card p{position:absolute;top:308px;left:20px;right:20px;text-align:center;font-size:15px;line-height:21px;color:var(--muted)}
.card .price{left:12px;top:380px;width:148px;height:38px;justify-content:flex-start;padding-left:20px;font-style:italic;font-size:19px}
.card .buy{left:173px;top:380px;width:148px;height:38px;font-size:18px}
.tone-jar{background:linear-gradient(135deg,#5a5650,#2f2b27 55%,#6f6a5d)}
.tone-seed{background:linear-gradient(135deg,#8c8880,#3f3c36 60%,#a29c90)}
.tone-fiber{background:linear-gradient(135deg,#d9c7ae,#9c7548 50%,#3b5f22 75%,#e5d6c2)}
.tone-glove{background:linear-gradient(135deg,#2f4d1f,#5e8f3a 45%,#b4d4e8 70%,#233b17)}
.tone-oil{background:linear-gradient(135deg,#2d2f3a,#3a3d4a 50%,#b89a3c 75%,#2d2f3a)}

/* features */
.features{height:753px;background:var(--white)}
.features .photo{left:120px;top:118px;width:406px;height:554px;border-radius:14px;background:radial-gradient(circle at 45% 40%,#3e7a28,#1c3d13 60%,#0c1d08)}
.features h2{left:615px;top:124px;width:420px;font-size:31px;line-height:38px;font-weight:500;color:var(--green)}
.feature{position:absolute;left:618px;width:460px;display:flex;gap:20px;align-items:flex-start;font-size:15.5px;line-height:24px;color:var(--text)}
.feature svg{flex:0 0 50px}
.features .start{left:618px;top:617px;width:204px;height:47px;font-size:20px}

/* testimonials */
.clients{height:524px;background:var(--light)}
.clients .section-title{top:62px}
.review{position:absolute;top:156px;width:445px;height:251px;background:var(--white);padding:40px 0 0 0}
.review .avatar{position:absolute;left:34px;top:40px;width:86px;height:86px;border-radius:50%}
.review .stars{position:absolute;left:152px;top:52px;color:var(--star);font-size:18px;letter-spacing:1px}
.review .name{position:absolute;left:152px;top:78px;font-size:19px;color:var(--text)}
.review .role{position:absolute;left:152px;top:108px;font-size:16px;font-style:italic;color:var(--text)}
.review p{position:absolute;left:40px;right:22px;top:150px;font-size:13.5px;line-height:20px;color:var(--muted)}

/* footer */
.site-footer{height:609px;background:var(--green-dark)}
.newsletter{position:absolute;left:125px;top:-47px;width:951px;height:169px;background:var(--olive);border-radius:8px}
.newsletter h2{position:absolute;left:60px;top:42px;font-size:30px;font-weight:500;color:var(--white)}
.newsletter p{position:absolute;left:60px;top:90px;width:330px;font-size:14px;line-height:18px;font-weight:500;color:var(--white)}
.signup{position:absolute;left:516px;top:55px;width:375px;height:60px;border:3px solid var(--white);border-radius:30px;background:var(--white);box-shadow:0 0 0 3px var(--olive) inset}
.signup span{position:absolute;left:24px;top:17px;font-size:15px;color:#999}
.signup .go{position:absolute;right:6px;top:6px;width:120px;height:42px;border-radius:21px;background:var(--olive);color:var(--white);display:flex;align-items:center;justify-content:center;font-size:15px}
.col-title{position:absolute;top:212px;font-size:21px;color:var(--olive);font-weight:500}
.col-title::after{content:"";position:absolute;left:0;top:45px;width:40px;height:3px;background:var(--white)}
.links{position:absolute;top:282px;list-style:none;font-size:15px;color:var(--white);line-height:31px}
.links li::before{content:"›";color:var(--olive);margin-right:14px;font-size:18px}
.contact{position:absolute;left:760px;width:330px;display:flex;gap:20px;align-items:center;color:var(--white);font-size:15px;line-height:19px}
.contact .ic{flex:0 0 32px;height:32px;border:2px solid var(--olive);border-radius:6px;display:flex;align-items:center;justify-content:center}
.bottom-line{position:absolute;left:0;top:501px;width:1200px;height:2px;background:var(--olive)}
.social{position:absolute;left:88px;top:535px;display:flex;gap:10px}
.social span{width:42px;height:42px;border:2.5px solid var(--olive);border-radius:50%}
.copy{position:absolute;right:90px;top:548px;font-size:15px;color:var(--white)}
</style>
</head>
<body>

<header class="site-header">
  <div class="abs brand"><span class="brand-dot"></span>Sunny Leaf</div>
  <nav class="abs nav">
    <a class="active" href="#">Home</a>
    <a href="#">Web Hosting</a>
    <a href="#">Reseller Hosting</a>
    <a href="#">Servers</a>
    <a href="#">Domain</a>
  </nav>
  <div class="btn account">My Account</div>
</header>

<section class="hero">
  <h1 class="abs">Cannabis products that are hemp derived and 100% legal across the US .</h1>
  <p class="abs">All cannabis is locally grown and products are extracted and made in house and sent out for third party lab testing.</p>
  <div class="btn btn-solid read">Read More</div>
  <div class="btn btn-outline products">Our Products</div>
  <div class="photo leaf" role="img" aria-label="Single green hemp leaf on a pale background"></div>
</section>

<section class="about">
  <div class="photo leafs" role="img" aria-label="Light green hemp leaves behind the round photo"></div>
  <div class="photo circle" role="img" aria-label="Hand holding a hemp leaf in a dark green field"></div>
  <h2 class="abs">About Sunny Leaf Hemp</h2>
  <p class="abs p1">Medical marijuana is a controversial topic for some, but the one thing that can’t it’s big business.</p>
  <p class="abs p2">Now legal in 36 US states,With figures like that, it’s clear to see that with the right tools, budding lucrative businesses.</p>
  <div class="btn btn-solid explore">Explore Now</div>
</section>

<section class="shop">
  <h2 class="section-title">Our Products</h2>
  <div class="tabs">
    <div class="tab active">All Hemp</div>
    <div class="tab">Edibles</div>
    <div class="tab">Concentrates</div>
    <div class="tab">THCA flower</div>
    <div class="tab">Vapes</div>
  </div>

  <article class="card" style="left:80px;top:279px">
    <div class="photo tone-jar" role="img" aria-label="Jar of hemp flower on a dark desk"></div>
    <h3>Hemp form CBD</h3>
    <p>There is no better way to choose the most active, lightweight foldable</p>
    <div class="btn btn-solid price">$ 34.99</div>
    <div class="btn btn-outline buy">Buy Now</div>
  </article>
  <article class="card" style="left:426px;top:279px">
    <div class="photo tone-seed" role="img" aria-label="Glass jar of hemp buds beside a pipe"></div>
    <h3>Hemp form Grain/Seed</h3>
    <p>There is no better way to choose the most active, lightweight foldable</p>
    <div class="btn btn-solid price">$ 16.99</div>
    <div class="btn btn-outline buy">Buy Now</div>
  </article>
  <article class="card" style="left:772px;top:279px">
    <div class="photo tone-fiber" role="img" aria-label="Oil bottle and hemp leaves on a wooden plate"></div>
    <h3>Hemp form Fiber</h3>
    <p>There is no better way to choose the most active, lightweight foldable</p>
    <div class="btn btn-solid price">$ 10.99</div>
    <div class="btn btn-outline buy">Buy Now</div>
  </article>

  <article class="card" style="left:80px;top:764px">
    <div class="photo tone-glove" role="img" aria-label="Gloved hand touching a hemp plant"></div>
    <h3>Greeny Hemp</h3>
    <p>There is no better way to choose the most active, lightweight foldable</p>
    <div class="btn btn-solid price">$ 34.99</div>
    <div class="btn btn-outline buy">Buy Now</div>
  </article>
  <article class="card" style="left:426px;top:764px">
    <div class="photo tone-jar" role="img" aria-label="Jar of hemp flower on a dark desk"></div>
    <h3>Marijuana.</h3>
    <p>There is no better way to choose the most active, lightweight foldable</p>
    <div class="btn btn-solid price">$ 16.99</div>
    <div class="btn btn-outline buy">Buy Now</div>
  </article>
  <article class="card" style="left:772px;top:764px">
    <div class="photo tone-oil" role="img" aria-label="Oil bottles, capsules and a hemp leaf on dark slate"></div>
    <h3>Cannabis sativa L.</h3>
    <p>There is no better way to choose the most active, lightweight foldable</p>
    <div class="btn btn-solid price">$ 10.99</div>
    <div class="btn btn-outline buy">Buy Now</div>
  </article>
</section>

<section class="features">
  <div class="photo" role="img" aria-label="Hand holding a hemp leaf against dark foliage"></div>
  <h2 class="abs">High Performance Hemp Are Available</h2>
  <div class="feature" style="top:223px">
    <svg width="50" height="50" viewBox="0 0 50 50"><circle cx="25" cy="25" r="24" fill="#4a7b35"/><path d="M14 26l8 8 15-17" fill="none" stroke="#fff" stroke-width="4" stroke-linecap="round" stroke-linejoin="round"/></svg>
    <span>We combine our great people with a truly collaborative approach .</span>
  </div>
  <div class="feature" style="top:309px">
    <svg width="50" height="50" viewBox="0 0 50 50"><circle cx="25" cy="25" r="24" fill="#4a7b35"/><path d="M14 26l8 8 15-17" fill="none" stroke="#fff" stroke-width="4" stroke-linecap="round" stroke-linejoin="round"/></svg>
    <span>From the moment we start working together, we’ll manage your technology</span>
  </div>
  <div class="feature" style="top:395px">
    <svg width="50" height="50" viewBox="0 0 50 50"><circle cx="25" cy="25" r="24" fill="#4a7b35"/><path d="M14 26l8 8 15-17" fill="none" stroke="#fff" stroke-width="4" stroke-linecap="round" stroke-linejoin="round"/></svg>
    <span>Projects, keep you updated, and take a proactive interest in helping your business</span>
  </div>
  <div class="feature" style="top:481px">
    <svg width="50" height="50" viewBox="0 0 50 50"><circle cx="25" cy="25" r="24" fill="#4a7b35"/><path d="M14 26l8 8 15-17" fill="none" stroke="#fff" stroke-width="4" stroke-linecap="round" stroke-linejoin="round"/></svg>
    <span>Our expert IT staff have many years of experience both across the IT sector and with important IT specialties.</span>
  </div>
  <div class="btn btn-solid start">Get Started</div>
</section>

<section class="clients">
  <h2 class="section-title">What The Client says</h2>
  <article class="review" style="left:156px">
    <div class="avatar" style="background:radial-gradient(circle,#b5562c,#5b2a17)" role="img" aria-label="Client portrait photo"></div>
    <div class="stars">★★★★★</div>
    <div class="name">Mara Quinn</div>
    <div class="role">Organiser</div>
    <p>Lorem ipsum dolor sit amet, consectetur adipiscing elit, sed do eiusmod tempor incididunt ut labore et dolore lacus vel facilisis.</p>
  </article>
  <article class="review" style="left:620px">
    <div class="avatar" style="background:radial-gradient(circle,#d9a51f,#3a3f4a)" role="img" aria-label="Client portrait photo"></div>
    <div class="stars">★★★★★</div>
    <div class="name">Theo Lark</div>
    <div class="role">Organiser</div>
    <p>Lorem ipsum dolor sit amet, consectetur adipiscing elit, sed do eiusmod tempor incididunt ut labore et dolore lacus vel facilisis.</p>
  </article>
</section>

<footer class="site-footer">
  <div class="newsletter">
    <h2>Newsletter Sign Up!</h2>
    <p>Lorem ipsum dolor sit amet, consectetur adipiscing elit, sed do eiusmod tempor</p>
    <div class="signup"><span>Email here</span><div class="go">SUMBIT</div></div>
  </div>

  <div class="col-title" style="left:208px">Quick Links</div>
  <ul class="links" style="left:212px">
    <li>Home</li><li>About Us</li><li>Our Services</li><li>Our Blogs</li><li>Testimonials</li>
  </ul>

  <div class="col-title" style="left:490px">Customer Services</div>
  <ul class="links" style="left:494px">
    <li>Contact us</li><li>Site Map</li><li>Terms and Use</li><li>My Account</li>
  </ul>

  <div class="col-title" style="left:758px">Our Newsletter</div>
  <div class="contact" style="top:284px">
    <div class="ic"><svg width="16" height="16" viewBox="0 0 24 24"><path d="M6 3l4 4-2 3c1 2 4 5 6 6l3-2 4 4-3 3C10 21 3 14 3 6z" fill="none" stroke="#7fa30d" stroke-width="2"/></svg></div>
    <div>CALL US<br>(555) 014-2290</div>
  </div>
  <div class="contact" style="top:340px">
    <div class="ic"><svg width="16" height="16" viewBox="0 0 24 24"><rect x="3" y="6" width="18" height="12" fill="none" stroke="#7fa30d" stroke-width="2"/><path d="M3 6l9 7 9-7" fill="none" stroke="#7fa30d" stroke-width="2"/></svg></div>
    <div>EMAIL US<br>hello@sunnyleafhemp.com</div>
  </div>
  <div class="contact" style="top:398px">
    <div class="ic"><svg width="16" height="16" viewBox="0 0 24 24"><path d="M12 22s7-7 7-12a7 7 0 0 0-14 0c0 5 7 12 7 12z" fill="none" stroke="#7fa30d" stroke-width="2"/><circle cx="12" cy="10" r="2.5" fill="#7fa30d"/></svg></div>
    <div>The dummy adress Is here<br>&amp;the Location</div>
  </div>

  <div class="bottom-line"></div>
  <div class="social"><span></span><span></span><span></span><span></span></div>
  <div class="copy">All Rights Reserved @ Copyrights 2023</div>
</footer>

</body>
</html>
```